Marla Kendrick Memoir

Book Cover Design
Title: Tundra and Smoke
Subtitle: One Daughter's Road Back to Kinship and Mercy
Author: Marla Kendrick
Book Description: Marla Kendrick’s memoir Tundra and Smoke, follows five generations of one Alaskan family evolving with the rapidly changing landscape of the North. Few memoirs combine love of nature with love of family so eloquently, while at the same time acknowledging that each carries the potential for so much loss and pain. Through it all, this is the story of one woman’s quest to carve a place for herself in a rapidly changing land and claim her own unique power.
INSTRUCTIONS: Open to any interesting creative designs reflecting the above description. However, MUST include the attached photo on the cover in some way. Have also attached the .indd template for reference. Please leave bleed area plus 1/2 inch all around. On spine, leave two inches at bottom to allow for publisher's logo.
Look and feel
Each slider illustrates characteristics of the customer's brand and the style your logo design should communicate.

```html
<!DOCTYPE html>
<html lang="en">
<head>
<meta charset="utf-8">
<title>Tundra and Smoke – Full Cover</title>
<link rel="stylesheet" href="https://fonts.googleapis.com/css2?family=Cinzel:wght@400;600&family=Crimson+Text:wght@400&family=EB+Garamond:wght@400;500&display=swap">
<style>
  :root {
    --sky-top: #a09282;
    --sky-mid: #b3a197;
    --haze: #cbbcb6;
    --mountain: #8f8aa0;
    --tree-red: #d9654f;
    --pine: #4a4240;
    --snow: #ddd6d8;
    --river: #6e6876;
    --ground: #6c5f66;
    --ground-deep: #3a3036;
    --ink-light: #ffffff;
    --photo-frame: #ffffff;
    --photo-fill: #7b7274;
  }
  html, body {
    margin: 0;
    padding: 0;
    overflow: hidden;
    background: #2e282c;
  }
  .cover {
    position: relative;
    width: 1200px;
    height: 862px;
    overflow: hidden;
    color: var(--ink-light);
  }
  .cover-art {
    position: absolute;
    inset: 0;
    width: 1200px;
    height: 862px;
  }

  /* Back panel */
  .back-title {
    position: absolute;
    left: 40px;
    top: 76px;
    width: 504px;
    margin: 0;
    text-align: center;
    font-family: "Cinzel", serif;
    font-weight: 400;
    font-size: 36px;
    letter-spacing: 0.06em;
    line-height: 1;
  }
  .back-blurb {
    position: absolute;
    left: 64px;
    top: 134px;
    width: 456px;
    font-family: "Crimson Text", serif;
    font-size: 16.2px;
    line-height: 19.7px;
    text-align: justify;
  }
  .back-blurb p { margin: 0 0 19.7px; }

  .author-photo {
    position: absolute;
    left: 62px;
    top: 521px;
    width: 108px;
    height: 123px;
    border: 10px solid var(--photo-frame);
    background: var(--photo-fill);
  }
  .author-bio {
    position: absolute;
    left: 224px;
    top: 520px;
    width: 304px;
    margin: 0;
    font-family: "Crimson Text", serif;
    font-size: 16.4px;
    line-height: 18.3px;
    text-align: justify;
  }

  /* Spine: text ends near 764px, leaving room at the foot for the publisher mark */
  .spine {
    position: absolute;
    left: 600px;
    top: 100px;
    width: 0;
    height: 0;
  }
  .spine-text {
    position: absolute;
    left: -18px;
    top: 0;
    transform-origin: 0 0;
    transform: rotate(90deg) translateY(-36px);
    white-space: nowrap;
    font-family: "Cinzel", serif;
    font-size: 29px;
    line-height: 36px;
    letter-spacing: 0.02em;
  }
  .spine-title { display: inline-block; width: 428px; }
  .spine-author { display: inline-block; font-size: 26px; }

  /* Front panel */
  .front-title {
    position: absolute;
    left: 660px;
    top: 88px;
    width: 500px;
    margin: 0;
    text-align: center;
    font-family: "Cinzel", serif;
    font-weight: 400;
    line-height: 1;
  }
  .front-title span { display: block; }
  .front-title .word-lead { font-size: 84px; letter-spacing: 0.06em; }
  .front-title .word-join { font-size: 58px; letter-spacing: 0.1em; margin-top: 14px; }
  .front-title .word-end { font-size: 88px; letter-spacing: 0.06em; margin-top: 12px; }

  .front-subtitle {
    position: absolute;
    left: 680px;
    top: 662px;
    width: 460px;
    margin: 0;
    text-align: center;
    font-family: "EB Garamond", serif;
    font-size: 25px;
    line-height: 27px;
    text-transform: uppercase;
    letter-spacing: -0.01em;
  }
  .front-author {
    position: absolute;
    left: 660px;
    top: 760px;
    width: 500px;
    margin: 0;
    text-align: center;
    font-family: "EB Garamond", serif;
    font-weight: 500;
    font-size: 40px;
    letter-spacing: 0.16em;
    text-transform: uppercase;
    line-height: 1;
  }
</style>
</head>
<body>
<div class="cover">
  <svg class="cover-art" viewBox="0 0 1200 862" role="img" aria-label="Painted winter landscape wrapping the whole cover: a red-leaved tree leaning over a snowy riverbank, dark pines on the right, misty mountains on the left and a winding river below">
    <defs>
      <linearGradient id="landscape-base" x1="0" y1="0" x2="0" y2="1">
        <stop offset="0" stop-color="var(--sky-top)"/>
        <stop offset="0.38" stop-color="var(--sky-mid)"/>
        <stop offset="0.55" stop-color="var(--haze)"/>
        <stop offset="0.8" stop-color="var(--ground)"/>
        <stop offset="1" stop-color="var(--ground-deep)"/>
      </linearGradient>
      <radialGradient id="tree-glow" cx="0.5" cy="0.5" r="0.5">
        <stop offset="0" stop-color="var(--tree-red)" stop-opacity="0.85"/>
        <stop offset="0.6" stop-color="var(--tree-red)" stop-opacity="0.4"/>
        <stop offset="1" stop-color="var(--tree-red)" stop-opacity="0"/>
      </radialGradient>
      <radialGradient id="pine-shade" cx="0.5" cy="0.5" r="0.5">
        <stop offset="0" stop-color="var(--pine)" stop-opacity="0.8"/>
        <stop offset="1" stop-color="var(--pine)" stop-opacity="0"/>
      </radialGradient>
      <radialGradient id="snow-light" cx="0.5" cy="0.5" r="0.5">
        <stop offset="0" stop-color="var(--snow)" stop-opacity="0.8"/>
        <stop offset="1" stop-color="var(--snow)" stop-opacity="0"/>
      </radialGradient>
      <radialGradient id="mountain-mist" cx="0.5" cy="0.5" r="0.5">
        <stop offset="0" stop-color="var(--mountain)" stop-opacity="0.7"/>
        <stop offset="1" stop-color="var(--mountain)" stop-opacity="0"/>
      </radialGradient>
      <radialGradient id="river-dark" cx="0.5" cy="0.5" r="0.5">
        <stop offset="0" stop-color="var(--river)" stop-opacity="0.8"/>
        <stop offset="1" stop-color="var(--river)" stop-opacity="0"/>
      </radialGradient>
    </defs>
    <rect width="1200" height="862" fill="url(#landscape-base)"/>
    <ellipse cx="180" cy="350" rx="240" ry="70" fill="url(#mountain-mist)"/>
    <ellipse cx="1090" cy="390" rx="170" ry="170" fill="url(#pine-shade)"/>
    <ellipse cx="880" cy="590" rx="330" ry="90" fill="url(#snow-light)"/>
    <ellipse cx="760" cy="720" rx="260" ry="70" fill="url(#river-dark)"/>
    <ellipse cx="560" cy="280" rx="270" ry="230" fill="url(#tree-glow)"/>
  </svg>

  <h2 class="back-title">TUNDRA AND SMOKE</h2>
  <div class="back-blurb">
    <p>Lorem ipsum dolor sit amet, consectetur adipiscing elit. Vivamus ipsum leo, vulputate in elementum ut, scelerisque id tortor. Sed odio odio, placerat ac metus at, pulvinar sodales tellus. Curabitur eu orci quis turpis rutrum scelerisque vel vel purus. Ut bibendum commodo risus, vel aliquam neque aliquam vehicula. Curabitur sit amet augue auctor, porttitor urna vel, facilisis arcu. Quisque eleifend pellentesque massa, sit amet dictum tellus lobortis non. Nullam vel ipsum ipsum. Aenean sed metus at urna efficitur molestie. Proin purus elit, vulputate eu rhoncus bibendum, maximus et nisl. Praesent finibus ullamcorper sodales.</p>
    <p>Nullam laoreet tincidunt nibh vel malesuada. In luctus ante quis nisi bibendum suscipit. Pellentesque sed elementum risus. Pellentesque ut erat felis. Cras nisi leo, semper in ullamcorper at, consequat in felis. Pellentesque molestie eu mauris a feugiat. Fusce blandit ultrices magna, dignissim feugiat nibh cursus in. Pellentesque non tristique nulla, at pulvinar urna. Mauris egestas eros sit amet lacinia fringilla. Proin tempus est at tortor fringilla consectetur.</p>
  </div>

  <div class="author-photo" role="img" aria-label="Author portrait"></div>
  <p class="author-bio">Lorem ipsum dolor sit amet, consectetur adipiscing elit, sed do eiusmod tempor incididunt ut labore et dolore magna aliqua. Quis ipsum suspendisse ultrices gravida. Risus commodo viverra maecenas accumsan lacus vel facilisis. Nullam laoreet tincidunt nibh vel malesuada. In luctus ante qbibendum suscipit ultrices gravida.</p>

  <div class="spine">
    <div class="spine-text"><span class="spine-title">TUNDRA AND SMOKE</span><span class="spine-author">MARLA KENDRICK</span></div>
  </div>

  <h1 class="front-title">
    <span class="word-lead">TUNDRA</span>
    <span class="word-join">AND</span>
    <span class="word-end">SMOKE</span>
  </h1>
  <p class="front-subtitle">One Daughter's Road Back to<br>Kinship and Mercy</p>
  <p class="front-author">Marla Kendrick</p>
</div>
</body>
</html>
```